National Chemical Line for Homeowners Needs a Logo & Label Design.

We need a logo and label design for a New National Chemical Company that is Private Labeling/Creating Cleaning Chemicals for Homeowners to use themselves. These chemicals will be used to clean carpets, hard surfaces, remove cat & dog stains and odors and many other products to come.
The first product will be for homeowners to remove cat & dog stains and odors from their carpets. We would like the label for the front and back of a 32 oz. white spray bottle. Go to www.brellowsupply.example and reference Part# 41KPL7.
We want the bottle/label to stand out on the grocery store shelves. We want it to be simple to read, eye catching, have a simple name and explain what the product does . The back of the bottle will have directions, caution statements, etc.
The Name of our Company is Vanta Meridian. It does have a trademark. We want the word "Vanta" to stand out and the word "meridian to only be present, that way the word Vanta will gain traction with the customer.
We want the color scheme to be Pinks & Blues.

```html
<!DOCTYPE html>
<html lang="en">
<head>
<meta charset="utf-8">
<title>Vanta Meridian – Carpets Restorer Label</title>
<link rel="stylesheet" href="https://fonts.googleapis.com/css2?family=Alfa+Slab+One&family=Oswald:wght@500&family=Source+Sans+3:wght@400;600;700;900&display=swap">
<style>
:root{
  --pink:#ec1f7a;
  --pink-soft:#f27db0;
  --pink-band:#c9417f;
  --navy:#2b2a86;
  --navy-deep:#231f6b;
  --sky:#25b5e4;
  --sky-deep:#1e86c0;
  --white:#ffffff;
  --ink:#1b1b1b;
  --gold:#e2b338;
  --page:#f4f4f6;
}
*{box-sizing:border-box;margin:0;padding:0}
html,body{width:1186px;height:1200px;overflow:hidden;background:var(--page)}
body{font-family:"Source Sans 3",sans-serif;position:relative}

.label{position:absolute;top:260px;width:540px;height:680px;background:var(--white);
  box-shadow:0 2px 10px rgba(0,0,0,.12);overflow:hidden}
.label--front{left:30px}
.label--back{left:616px}

.crest{height:118px;background:linear-gradient(90deg,var(--pink) 0%,var(--pink-soft) 40%,var(--pink) 100%);
  border-radius:270px 270px 0 0/118px 118px 0 0;position:relative}

/* front */
.tagline{height:34px;background:var(--pink-band);color:var(--white);font-size:18px;
  display:flex;align-items:center;justify-content:center;border-bottom:3px solid var(--white)}
.hero{position:relative;height:398px;overflow:hidden}
.hero__arcs{position:absolute;inset:0}
.hero__shield{position:absolute;left:168px;top:12px;width:200px;height:230px;
  border-radius:18px 18px 100px 100px;
  background:linear-gradient(160deg,#d9eef9 0%,#5aa7d8 55%,#9aa3ad 100%);opacity:.9}
.hero__germ{position:absolute;border-radius:50%;
  background:radial-gradient(circle,#e8f4fb 0%,#8fc4e4 60%,#6e9fc2 100%)}
.germ--a{left:40px;top:24px;width:60px;height:60px}
.germ--b{right:14px;top:26px;width:76px;height:76px}
.germ--c{left:26px;top:296px;width:54px;height:54px}
.brand-block{position:absolute;left:36px;top:96px;width:468px;height:160px;background:var(--navy);
  border:4px solid var(--white);border-radius:10px;display:flex;flex-direction:column;
  align-items:center;justify-content:center;color:var(--white);font-weight:900;line-height:1}
.brand-block__main{font-size:96px;letter-spacing:4px}
.brand-block__sub{font-size:34px;letter-spacing:6px;margin-top:6px}
.tm{position:absolute;right:40px;top:262px;color:var(--navy);font-size:14px}
.product{position:absolute;left:0;right:0;top:284px;text-align:center}
.product__kicker{font-family:"Alfa Slab One",serif;font-size:24px;color:var(--white);
  -webkit-text-stroke:1px var(--navy);paint-order:stroke fill}
.product__name{font-family:"Alfa Slab One",serif;font-size:34px;color:var(--white);
  -webkit-text-stroke:3px var(--navy);paint-order:stroke fill;word-spacing:12px;line-height:1.1}
.product__claim{font-weight:700;font-size:19px;color:var(--pink);
  -webkit-text-stroke:3px var(--white);paint-order:stroke fill}
.front-foot{height:130px;background:var(--navy);display:flex;align-items:center;padding:0 22px;gap:20px;color:var(--white)}
.seal{width:82px;height:82px;border-radius:50%;background:radial-gradient(circle,var(--gold) 0 55%,#1a1a1a 56% 70%,var(--gold) 71%);flex:none}
.caution-block{font-family:"Oswald",sans-serif;font-size:25px;line-height:1.35;flex:1}
.volume{font-family:"Oswald",sans-serif;font-size:21px;line-height:1.5;text-align:center}

/* back */
.crest--back{height:160px;border-radius:270px 270px 0 0/150px 150px 0 0;display:flex;align-items:flex-end;
  justify-content:center;padding-bottom:26px;gap:12px}
.crest__dot{width:34px;height:34px;border-radius:50%;background:var(--white)}
.crest__name{font-weight:900;font-size:38px;color:var(--navy);letter-spacing:1px;line-height:1}
.panel{padding:12px 16px 0 20px;font-size:11.6px;line-height:1.38;color:var(--ink)}
.panel__title{text-align:center;line-height:1.05;margin-bottom:6px}
.panel__kicker{font-family:"Alfa Slab One",serif;color:var(--navy);font-size:17px}
.panel__name{font-family:"Alfa Slab One",serif;color:var(--pink);font-size:24px;word-spacing:10px}
.panel__claim{font-weight:700;color:var(--navy);font-size:14px}
.panel p{margin-bottom:10px}
.accent{color:var(--pink)}
.panel strong{font-weight:700}
.guarantee{position:absolute;left:0;right:0;bottom:0;height:112px;background:linear-gradient(90deg,var(--navy),var(--navy-deep));
  color:var(--white);font-size:16px;line-height:1.4;padding:18px 22px}
.guarantee strong{font-weight:600}
</style>
</head>
<body>

<section class="label label--front">
  <div class="crest"></div>
  <div class="tagline">Cleaning Chemicals for Homeowners to use themselves</div>
  <div class="hero">
    <svg class="hero__arcs" width="540" height="398" viewBox="0 0 540 398" aria-hidden="true">
      <rect width="540" height="398" fill="#ffffff"/>
      <rect x="0" y="0" width="540" height="160" fill="#eaf5fb"/>
      <path d="M0 150 H270 V398 H0Z" fill="#f3b8d2"/>
      <path d="M270 150 H540 V398 H270Z" fill="#a9cfe6"/>
      <circle cx="270" cy="470" r="300" fill="#ec6aa5"/>
      <path d="M270 170 A300 300 0 0 1 570 470 H270Z" fill="#4fa6d6"/>
      <circle cx="270" cy="470" r="255" fill="#ffffff"/>
      <circle cx="270" cy="470" r="240" fill="#e93f8c"/>
      <path d="M270 230 A240 240 0 0 1 510 470 H270Z" fill="#1e86c0"/>
      <circle cx="270" cy="470" r="190" fill="#ffffff"/>
      <circle cx="270" cy="470" r="176" fill="#25b5e4"/>
    </svg>
    <div class="hero__shield" role="img" aria-label="Glossy blue protective shield illustration"></div>
    <div class="hero__germ germ--a" role="img" aria-label="Pale blue germ illustration"></div>
    <div class="hero__germ germ--b" role="img" aria-label="Pale blue germ illustration"></div>
    <div class="hero__germ germ--c" role="img" aria-label="Pale blue germ illustration"></div>
    <div class="brand-block">
      <span class="brand-block__main">VANTA</span>
      <span class="brand-block__sub">MERIDIAN</span>
    </div>
    <span class="tm">TM</span>
    <div class="product">
      <div class="product__kicker">The Solutions</div>
      <div class="product__name">Carpets Restorer</div>
      <div class="product__claim">REMOVE CAT &amp; DOG STAINS AND ODORS</div>
    </div>
  </div>
  <div class="front-foot">
    <div class="seal" role="img" aria-label="Gold award seal"></div>
    <div class="caution-block">CAUTION : EYE IRRITANT.<br>Read back panel carefully.</div>
    <div class="volume">32 FL OZ<br>(1 QT) 946 ml</div>
  </div>
</section>

<section class="label label--back">
  <div class="crest crest--back">
    <span class="crest__dot"></span>
    <span class="crest__name">VANTA MERIDIAN</span>
  </div>
  <div class="panel">
    <div class="panel__title">
      <div class="panel__kicker">The Solutions</div>
      <div class="panel__name">Carpets Restorer</div>
      <div class="panel__claim">REMOVE CAT &amp; DOG STAINS AND ODORS</div>
    </div>
    <p><span class="accent">Bio-enzymatic formula uses BX40 Technology</span> to eliminate organic matter and odors. Friendly bacteria create enzymes, which break down the organic matter, eliminating stains and odors.</p>
    <p><strong>Great for use on: urinals, toilets, tile floors &amp; grout, hard &amp; soft surfaces, carpet &amp; upholstery, and pet urine stains.</strong> Not recommended for silk, leather or suede.</p>
    <p><span class="accent">DIRECTIONS-</span><strong>Cleaning carpets or upholstery:</strong> Remove excess solid or liquid waste.</p>
    <p>Test on a hidden area for color fastness. Spray and soak the stained area, then scrub. Cover the area with a wet wash cloth. For best results, leave overnight and let the enzymes do their work. Remove or repeat as needed.<br><strong>Cleaning concrete, tile, grout or wood floors:</strong> Saturate the stained area by spraying product, then wipe off. Repeat as needed.</p>
    <p><span class="accent">CAUTION:</span> Keep out of reach of children. Not for internal consumption. Avoid prolonged contact with skin. May cause temporary irritation. If ingested, consult a physician. Avoid contact with eyes. If product comes into contact with eyes, flush immediately with water and consult a physician. <em>Contains live bacterial cultures, surfactant blend, and fragrance.</em></p>
    <p><strong>No animal testing. No phosphates. No harsh chemicals or solvents.</strong></p>
  </div>
  <div class="guarantee"><strong>Guarantee:</strong> If not satisfied, mail or email receipt along with company name, address and a brief description for a full refund of your purchase price. Allow 4 weeks for delivery</div>
</section>

</body>
</html>
```